Medical Services company. Need a website that blows the competition out of the water

We need a web site designed to draw attention to our many services offered. We are a Medical Services business based out of Pennsylvania. We provide basic first aid staffing for events and businesses such as but not limited to: Fairs, Festivals, Carnivals, Sporting events, Large gatherings where a first aid station is needed, Concerts, Businesses with first aid needs . We provide training and certifications that are tailored to the customers needs. We provide Covid-19 pre screening and temperature monitoring. Our professionals consist of individuals with Basic First Aid, Certified Nursing Assistants, Medical Assistants, Emergency Medical Responders (EMR), Emergency Medical Technicians (EMT), and Nurses. I do not know how many pages I will need since we offer multiple different services. Our main services provided are: First Aid services, Covid-19 pre screen and temperatures, and Training/Certifications. You will have to use stock photos for now until I can get some actual photographs of our team.I have uploaded a copy of my brochure so you can get some information from there as well.

Target Market(s)

-For the first Aid and Covid-19 services: All Businesses, Sporting events, Event organizers
-Training: Everyone.

Coding

Number of Pages Required

Font styles to use
Sans Serif

Requirements
Must have
• My colors are what is in the logos and Gray , need to have a way for customers to request a quote, design that grabs their attention. Should have pictures of medical providers attending to the sick or injured. Both in a office setting and in an emergency out in public. Should have pictures of an ambulance. Should also have pictures of staff taking temperatures and asking pre screening questions.
Nice to have
• I'll get back to you on that one

```html
<!DOCTYPE html>
<html lang="en">
<head>
<meta charset="utf-8">
<title>KMS Medical Services</title>
<link href="https://fonts.googleapis.com/css2?family=Poppins:wght@400;500;600;700&family=Montserrat:wght@700;800&family=Roboto+Condensed:wght@700&display=swap" rel="stylesheet">
<style>
:root{
  --blue:#2d3ca3;
  --blue-deep:#23308a;
  --teal:#17ab9c;
  --ink:#333;
  --muted:#555;
  --light:#f6f6f6;
  --footer:#5a5a5c;
  --white:#fff;
}
*{margin:0;padding:0;box-sizing:border-box}
html,body{width:1200px;height:4815px;overflow:hidden}
body{position:relative;font-family:"Poppins",sans-serif;color:var(--ink);background:var(--white)}
.abs{position:absolute}
a{color:inherit;text-decoration:none}

/* header */
.topbar{position:absolute;right:0;top:0;width:390px;height:24px;background:var(--blue-deep);clip-path:polygon(20px 0,100% 0,100% 100%,0 100%);color:#fff;font-size:11px;display:flex;gap:16px;align-items:center;padding-left:44px}
.topbar span::before{content:"";display:inline-block;width:7px;height:7px;border-radius:50%;background:var(--teal);margin-right:6px}
.brand{position:absolute;left:88px;top:14px;display:flex;align-items:center;gap:8px}
.brand-dot{width:44px;height:44px;border-radius:50%;background:var(--blue)}
.brand-name{font-family:"Poppins",sans-serif;font-weight:700;font-size:34px;color:var(--blue);line-height:1}
.brand-name small{display:block;font-size:10px;font-weight:700;color:var(--blue);margin-top:2px}
.nav{position:absolute;right:90px;top:44px;display:flex;gap:30px;font-size:14px;font-weight:500;color:#222}
.nav .active{color:var(--teal)}

/* hero */
.hero{position:absolute;left:0;top:78px;width:1200px;height:762px;background:linear-gradient(110deg,#4a4d55 0%,#3b4f78 45%,#26407a 70%,#6f7b8a 100%)}
.hero h1{position:absolute;left:88px;top:258px;font-family:"Montserrat",sans-serif;font-weight:800;font-size:44px;line-height:46px;color:#fff}
.btn-teal{display:inline-block;background:var(--teal);color:#fff;font-size:13px;font-weight:700;border-radius:22px;padding:12px 20px;text-transform:uppercase}
.hero .btn-teal{position:absolute;left:88px;top:412px}
.scroll{position:absolute;left:590px;top:612px;width:18px;height:28px;border:2px solid #fff;border-radius:9px}
.hero-wave{position:absolute;left:0;top:620px}

/* about */
.about-photo{position:absolute;left:106px;top:874px;width:438px;height:438px;border-radius:50%;background:linear-gradient(135deg,#1aae9f,#5b8fb0 40%,#9aa8b8)}
.about-photo2{position:absolute;left:374px;top:1135px;width:186px;height:186px;border-radius:50%;background:linear-gradient(135deg,#e9ecef,#8f959c);border:6px solid #fff}
.eyebrow{font-size:18px;font-weight:700;color:var(--blue);text-transform:uppercase}
.title{font-family:"Roboto Condensed",sans-serif;font-weight:700;font-size:42px;color:#3a3a3a;text-transform:uppercase;line-height:1.05}
.about-text{position:absolute;left:632px;top:1003px;width:490px}
.about-text p{font-size:14.5px;line-height:25px;color:var(--muted);margin-top:10px}
.btn-line{display:inline-block;border:2px solid var(--teal);border-radius:20px;padding:7px 20px;font-size:13px;font-weight:700;color:#333;margin-top:14px}

/* services */
.grey-band{position:absolute;left:0;top:1360px;width:1200px;height:900px}
.center{position:absolute;left:0;width:1200px;text-align:center}
.services-intro{font-size:14.5px;line-height:23px;color:var(--muted)}
.hub{position:absolute;left:421px;top:1707px;width:362px;height:362px;border-radius:50%;background:#fff;border:1px solid #e4e4e4;display:flex;align-items:center;justify-content:center}
.hub-mark{width:230px;height:230px;border-radius:50%;background:var(--blue);display:flex;align-items:center;justify-content:center;color:#fff;font-weight:700;font-size:54px}
.svc-icon{position:absolute;width:78px;height:78px;border-radius:50%;background:#fff;border:1px solid #e2e2e2;box-shadow:0 4px 12px rgba(0,0,0,.08);display:flex;align-items:center;justify-content:center}
.svc{position:absolute;width:290px}
.svc h3{font-size:19px;font-weight:600;color:var(--blue);margin-bottom:6px}
.svc p{font-size:14px;line-height:23px;color:var(--muted)}
.svc.left{text-align:right}

/* provide */
.provide{position:absolute;left:0;top:2120px;width:1200px;height:790px}
.provide h2{color:#fff}
.card{position:absolute;top:2467px;width:246px;height:322px;border:3px solid rgba(255,255,255,.85)}
.card .label{position:absolute;left:14px;right:14px;bottom:16px;height:52px;background:#fff;border-radius:4px;display:flex;align-items:center;justify-content:center;font-weight:600;font-size:19px;color:#333}
.card .label.teal{background:var(--teal);color:#fff}

/* events */
.ev-big{position:absolute;left:86px;top:3112px;width:500px;height:462px;background:#fff;box-shadow:0 8px 24px rgba(0,0,0,.1)}
.ev-small{position:absolute;left:606px;width:500px;height:225px;background:#fff;box-shadow:0 8px 24px rgba(0,0,0,.1)}
.ev-small.teal{background:var(--teal);color:#fff}
.ev-img{position:absolute;left:0;top:0}
.ev-body{position:absolute}
.ev-body h4{font-size:19px;font-weight:500;margin-bottom:6px}
.ev-body p{font-size:11.5px;line-height:19px}
.ev-body .more{font-size:11.5px;font-weight:600;margin-top:4px}

/* testimonials */
.orbit{position:absolute;border-radius:50%;border:1.5px solid #e3e3e3}
.avatar{position:absolute;border-radius:50%;border:4px solid #fff;box-shadow:0 4px 10px rgba(0,0,0,.15)}
.testi{position:absolute;left:611px;top:3880px;width:500px}
.testi p{font-size:14px;line-height:23px;color:var(--muted);margin-top:18px}
.testi .who{font-size:14px;font-weight:700;color:#444;margin-top:22px}

/* footer */
.footer-bg{position:absolute;left:0;top:4240px}
.foot-brand{position:absolute;left:88px;top:4578px;display:flex;align-items:center;gap:10px;color:#fff;font-weight:700;font-size:54px;line-height:1}
.foot-brand .dot{width:64px;height:64px;border-radius:50%;background:#fff}
.foot-brand small{display:block;font-size:13px;font-weight:500;margin-top:2px}
.fcol{position:absolute;top:4497px;color:#fff}
.fcol h5{font-size:21px;font-weight:600;margin-bottom:8px}
.fcol li{list-style:none;font-size:12.5px;line-height:25px}
.email-field{width:272px;height:42px;border-radius:21px;background:#707072;color:#eee;font-size:14px;padding:11px 22px;margin-top:12px}
.btn-sub{display:inline-block;background:var(--teal);color:#fff;font-weight:700;font-size:15px;border-radius:22px;padding:10px 24px;margin-top:12px}
.contact li{display:flex;align-items:center;gap:8px}
.contact li i{display:inline-block;width:9px;height:9px;border-radius:50%;background:var(--teal)}
.social{display:flex;gap:14px;margin-top:8px}
.social span{width:12px;height:12px;border-radius:50%;background:#fff}
.divider{position:absolute;left:88px;top:4747px;width:1024px;height:1px;background:#777}
.copy{position:absolute;left:0;top:4780px;width:1200px;text-align:center;color:#fff;font-size:13px}
.to-top{position:absolute;left:1124px;top:4756px;width:38px;height:38px;border-radius:50%;background:var(--blue);display:flex;align-items:center;justify-content:center}
</style>
</head>
<body>

<header>
  <div class="topbar"><span>555-014-2273</span><span>team@kmsmedic.com</span></div>
  <div class="brand"><div class="brand-dot"></div><div class="brand-name">KMS<small>Medical Services</small></div></div>
  <nav class="nav"><a class="active">Home</a><a>About</a><a>Services</a><a>Our Staff</a><a>Events</a><a>Contact us</a></nav>
</header>

<section class="hero" role="img" aria-label="Paramedics giving oxygen to a patient inside an ambulance">
  <h1>Provding all of<br>your health and<br>safety needs</h1>
  <a class="btn-teal">Contact us</a>
  <div class="scroll"></div>
  <svg class="hero-wave" width="1200" height="142" viewBox="0 0 1200 142">
    <path d="M0 80 C200 -10 330 40 520 70 C760 110 980 110 1200 40 L1200 142 L0 142Z" fill="#2d3ca3"/>
    <path d="M0 142 L0 120 C180 20 360 50 560 80 C800 118 1000 108 1200 70 L1200 142Z" fill="#fff"/>
  </svg>
</section>

<section class="about">
  <div class="about-photo" role="img" aria-label="Paramedic attending to a patient"></div>
  <div class="about-photo2" role="img" aria-label="Ambulance parked outside"></div>
  <div class="about-text">
    <div class="eyebrow">About us</div>
    <h2 class="title">Keeping you safe</h2>
    <p>You will notice the difference when you choose KMS for your business or event.</p>
    <p>By having trained, professional, responders present, your staff will feel safer and morale will improve, productivity will increase, and incidents will reduce.</p>
    <a class="btn-line">READ MORE</a>
  </div>
</section>

<svg class="grey-band" viewBox="0 0 1200 900" preserveAspectRatio="none">
  <path d="M0 60 C250 130 450 110 700 50 C900 5 1080 10 1200 40 L1200 780 C1000 790 850 840 650 880 C400 920 150 860 0 840Z" fill="#f6f6f6"/>
</svg>

<section class="services">
  <div class="center eyebrow" style="top:1560px">KMS services</div>
  <h2 class="center title" style="top:1585px">Training services</h2>
  <p class="center services-intro" style="top:1637px">At KMS we have a broad range of Health and  Safety classes to suit your every need. We take  pride in<br>our instructors who have years of experience instructing quality built classes.</p>

  <div class="hub"><div class="hub-mark">KMS</div></div>

  <div class="svc-icon" style="left:385px;top:1751px"><svg width="30" height="30" viewBox="0 0 30 30"><rect x="3" y="8" width="24" height="18" rx="3" fill="#2d3ca3"/><rect x="11" y="4" width="8" height="5" rx="1" fill="none" stroke="#2d3ca3" stroke-width="2"/><path d="M15 12v10M10 17h10" stroke="#fff" stroke-width="3"/></svg></div>
  <div class="svc-icon" style="left:735px;top:1751px"><svg width="30" height="30" viewBox="0 0 30 30"><path d="M15 27 C5 19 2 14 2 9 A6.5 6.5 0 0 1 15 7 A6.5 6.5 0 0 1 28 9 C28 14 25 19 15 27Z" fill="#2d3ca3"/><path d="M16 9 L11 17 H16 L13 23 L20 14 H15Z" fill="#fff"/></svg></div>
  <div class="svc-icon" style="left:385px;top:1931px"><svg width="32" height="32" viewBox="0 0 32 32"><circle cx="17" cy="16" r="11" fill="none" stroke="#2d3ca3" stroke-width="2"/><path d="M17 10v12M11 16h12" stroke="#2d3ca3" stroke-width="3"/><path d="M2 12h6M1 16h6M2 20h6" stroke="#2d3ca3" stroke-width="2"/></svg></div>
  <div class="svc-icon" style="left:735px;top:1931px"><svg width="32" height="32" viewBox="0 0 32 32"><circle cx="12" cy="18" r="7" fill="#2d3ca3"/><circle cx="23" cy="10" r="5" fill="#2d3ca3"/><circle cx="24" cy="23" r="3" fill="#2d3ca3"/><g stroke="#2d3ca3" stroke-width="2"><path d="M12 8v3M12 25v3M2 18h3M19 18h3"/></g></svg></div>

  <div class="svc left" style="left:60px;top:1750px"><h3>First Aid</h3><p>For patients with minor<br>to life threatening injuries<br>or illness</p></div>
  <div class="svc" style="left:834px;top:1750px;width:300px"><h3>Trauma/Resuscitation</h3><p>Provide Immediate and LIFE SAVING treatment for patients with Life  Threat-ening injuries or illness</p></div>
  <div class="svc left" style="left:60px;top:1932px"><h3>Onsite Care</h3><p>Provide immediate care by remov-ing the delay in response, assess-ment and  treatment</p></div>
  <div class="svc" style="left:834px;top:1932px;width:270px"><h3>Covid-19 Pre Screening</h3><p>Pre Screening and Temperature Monitoring of Individuals entering your facility or event</p></div>
</section>

<svg class="provide" viewBox="0 0 1200 790" preserveAspectRatio="none">
  <path d="M0 90 C200 50 400 95 600 95 C850 95 1050 40 1200 0 L1200 790 L0 790Z" fill="#2d3ca3"/>
</svg>
<section>
  <h2 class="center title" style="top:2344px;color:#fff">We provide</h2>
  <p class="center" style="top:2400px;color:#fff;font-size:14.5px;line-height:23px">basic first aid and Covid-19 Pre screening and temperature<br>monitoring for, but  not limited to:</p>
  <div class="card" style="left:88px;background:linear-gradient(160deg,#6c7aa8,#c4734a)" role="img" aria-label="Medic treating a person at a party with balloons"><div class="label">Special Events</div></div>
  <div class="card" style="left:348px;background:linear-gradient(160deg,#b0a49a,#d8c27a)" role="img" aria-label="Woman wearing a face mask at work"><div class="label teal">Business</div></div>
  <div class="card" style="left:606px;background:linear-gradient(160deg,#c9d6e4,#3f6fb0)" role="img" aria-label="Rescuers carrying a stretcher in snow"><div class="label">Sporting Events</div></div>
  <div class="card" style="left:864px;background:linear-gradient(160deg,#9aa0a5,#5c6a70)" role="img" aria-label="Group of people wearing masks"><div class="label">Large Gatherings</div></div>
</section>

<section class="events">
  <div class="center eyebrow" style="top:3015px">KMS Event</div>
  <h2 class="center title" style="top:3040px">Latest events</h2>

  <article class="ev-big">
    <div class="ev-img" role="img" aria-label="Hands performing chest compressions on a training dummy" style="width:500px;height:342px;background:linear-gradient(135deg,#c7512a,#6b6e74 55%,#3a3d44)"></div>
    <div class="ev-body" style="left:38px;top:372px;width:440px;color:#333"><h4>Event Heading here</h4><p>Lorem Ipsum is simply dummy text of the printing and typesetting industry.<br>Lorem Ipsum has been the industry's .</p></div>
  </article>

  <article class="ev-small" style="top:3112px">
    <div class="ev-img" role="img" aria-label="Patient loaded into an ambulance" style="width:271px;height:225px;background:linear-gradient(135deg,#d9dde2,#5477a8 60%,#d8c53a)"></div>
    <div class="ev-body" style="left:296px;top:48px;width:190px;color:#333"><h4>Event Heading here</h4><p>Lorem Ipsum is simply dummy text of the printing and typeset-ting industry. Lorem Ipsum has been the industry's .</p><div class="more">Read More</div></div>
  </article>

  <article class="ev-small teal" style="top:3349px">
    <div class="ev-img" role="img" aria-label="Medics with equipment bags on a field" style="width:271px;height:225px;background:linear-gradient(135deg,#6e9a4a,#2f4630 55%,#b83a3a)"></div>
    <div class="ev-body" style="left:296px;top:48px;width:190px"><h4>Event Heading here</h4><p>Lorem Ipsum is simply dummy text of the printing and typeset-ting industry. Lorem Ipsum has been the industry's .</p><div class="more">Read More</div></div>
  </article>
</section>

<section class="testimonials">
  <div class="orbit" style="left:0;top:3690px;width:550px;height:550px"></div>
  <div class="orbit" style="left:82px;top:3812px;width:340px;height:340px"></div>
  <div class="orbit" style="left:198px;top:3928px;width:150px;height:150px"></div>
  <div class="avatar" style="left:357px;top:3810px;width:170px;height:170px;background:linear-gradient(135deg,#7a5d4e,#2f3542)" role="img" aria-label="Client portrait, active"></div>
  <div class="avatar" style="left:64px;top:4008px;width:104px;height:104px;background:#7a6a62" role="img" aria-label="Client portrait"></div>
  <div class="avatar" style="left:203px;top:4060px;width:130px;height:130px;background:#d6b9a4" role="img" aria-label="Client portrait"></div>
  <div class="avatar" style="left:242px;top:3924px;width:58px;height:58px;background:#a9b2b8" role="img" aria-label="Client portrait"></div>
  <div class="avatar" style="left:380px;top:4047px;width:72px;height:72px;background:#3f9aa0" role="img" aria-label="Client portrait"></div>
  <div class="avatar" style="left:175px;top:3738px;width:40px;height:40px;background:#8a6e60" role="img" aria-label="Client portrait"></div>
  <div class="avatar" style="left:420px;top:3693px;width:42px;height:42px;background:#c07a55" role="img" aria-label="Client portrait"></div>
  <div class="avatar" style="left:435px;top:4168px;width:44px;height:44px;background:#5a5450" role="img" aria-label="Client portrait"></div>
  <div class="avatar" style="left:145px;top:4178px;width:64px;height:64px;background:#6f6a66" role="img" aria-label="Client portrait"></div>

  <div class="testi">
    <h2 class="title">Client<br>testimonials</h2>
    <p>Lorem Ipsum is simply dummy text of the printing and typesetting indus-try. Lorem Ipsum has been the industry's standard dummy text ever since the 1500s, when an unknown printer took a galley of type and scrambled it to make a type specimen book.</p>
    <div class="who">- DAN PORTER</div>
    <svg width="80" height="20" viewBox="0 0 80 20" style="margin-top:18px"><path d="M24 10H2M8 4L2 10L8 16" stroke="#aaa" stroke-width="1.5" fill="none"/><path d="M34 10H78M72 4L78 10L72 16" stroke="#333" stroke-width="1.5" fill="none"/></svg>
  </div>
</section>

<svg class="footer-bg" width="1200" height="575" viewBox="0 0 1200 575">
  <path d="M0 30 C200 110 420 140 650 100 C880 60 1050 20 1200 0 L1200 575 L0 575Z" fill="#2d3ca3"/>
  <path d="M0 70 C220 140 450 160 680 120 C900 82 1060 60 1200 50 L1200 575 L0 575Z" fill="#5a5a5c"/>
</svg>
<footer>
  <div class="foot-brand"><div class="dot"></div><div>KMS<small>Medical Services</small></div></div>
  <div class="fcol" style="left:385px"><h5>Useful Links</h5><ul><li>Home</li><li>About</li><li>Services</li><li>Our Staff</li><li>Events</li><li>Contact us</li></ul></div>
  <div class="fcol" style="left:592px"><h5>Newsletter</h5><ul><li>Subscribe to our newsletter</li></ul><div class="email-field">Email Address</div><a class="btn-sub">SUBSCRIBE</a></div>
  <div class="fcol contact" style="left:905px"><h5>Contact Us</h5><ul><li><i></i>555-014-2273</li><li><i></i>team@kmsmedic.com</li><li><i></i>www.kmsmedic.com</li></ul><div class="social"><span></span><span></span><span></span><span></span></div></div>
  <div class="divider"></div>
  <div class="copy">Copyright 2020 | All Rights Reserved</div>
  <div class="to-top"><svg width="14" height="10" viewBox="0 0 14 10"><path d="M2 8L7 3L12 8" stroke="#fff" stroke-width="2" fill="none"/></svg></div>
</footer>

</body>
</html>
```